Presentation Folder

Design presentation folder for professional law firm. Our law firm primarily represents individuals who are dealing with divorce, child custody, child support, spousal support, wills, estates and other civil litigation.
We desire a simple, professional, but memorable presentation folder that we can give clients containing their important documents (e.g., contract, and other important papers). The folder will also have a place for a business card. We will print this at Prindlebay. Specs and Templates are available at http://www.prindlebay-example.com/vp/ns/propath/UploadResources.aspx?selectedTab=0?pfid=156&pf_id=156&xnav=studio-side-bar#Templates
Our logo and one of our business cards is attached.
Our website is www.HolloweyFamilyLaw-example.com
Target Market(s)
Individual with legal issues primarily undergoing divorce
Industry/Entity Type
Law Firm
Font styles to use
Other font styles liked:
- Tahoma
Look and feel

```html
<!DOCTYPE html>
<html lang="en">
<head>
<meta charset="utf-8">
<title>Hollowey Law – Presentation Folder</title>
<link rel="stylesheet" href="https://fonts.googleapis.com/css2?family=Noto+Sans:wght@400;700&display=swap">
<style>
  :root {
    --canvas: #d4d4d4;
    --navy: #2f3a6e;
    --gold: #e9bb3c;
    --ink-light: #f2d27a;
  }
  * { box-sizing: border-box; margin: 0; padding: 0; }
  html, body { width: 1200px; height: 1000px; overflow: hidden; }
  body {
    background: var(--canvas);
    font-family: "Noto Sans", Tahoma, sans-serif;
    position: relative;
  }
  .folder-spread {
    position: absolute;
    left: 30px; top: 120px;
    width: 1140px; height: 760px;
    display: flex;
    box-shadow: 0 6px 18px rgba(0,0,0,.18);
  }
  .panel {
    position: relative;
    width: 570px; height: 760px;
    background: var(--navy);
  }
  .panel--back { border-right: 1px solid rgba(0,0,0,.18); }
  .edge-band {
    position: absolute; top: 0; bottom: 0;
    width: 28px; background: var(--gold);
  }
  .panel--back .edge-band { left: 0; }
  .panel--front .edge-band { right: 0; }
  .edge-mark {
    position: absolute; width: 14px; height: 14px;
    background: #ffffff; border: 2px solid var(--navy);
    left: 7px;
  }
  .panel--back .edge-mark { top: 14px; }
  .panel--front .edge-mark { bottom: 14px; }

  .brand {
    display: flex; align-items: center; gap: 8px;
    color: var(--gold); font-weight: 700; letter-spacing: .06em;
    text-transform: uppercase;
  }
  .brand__square { background: var(--gold); flex: none; }

  .front-lockup {
    position: absolute; top: 70px; left: 130px; width: 320px;
    text-align: center;
  }
  .front-lockup .brand { justify-content: center; font-size: 22px; }
  .front-lockup .brand__square { width: 18px; height: 18px; }
  .tagline {
    margin-top: 18px; color: var(--gold);
    font-size: 14px; line-height: 1.35;
  }

  .contact-block {
    position: absolute; left: 50px; bottom: 40px;
    color: var(--ink-light); font-size: 8px; line-height: 1.5;
    font-style: normal;
  }
  .contact-block .brand { font-size: 12px; margin-bottom: 8px; }
  .contact-block .brand__square { width: 12px; height: 12px; }
  .contact-block__firm { font-weight: 700; font-size: 9px; color: var(--gold); }
</style>
</head>
<body>
  <main class="folder-spread">
    <section class="panel panel--back">
      <div class="edge-band"><span class="edge-mark"></span></div>
      <address class="contact-block">
        <div class="brand"><span class="brand__square"></span>Hollowey Law</div>
        <p class="contact-block__firm">Hollowey Law, PLLC</p>
        <p>218 Harbor Lane, Suite C, PO Box 412</p>
        <p>Brookfield, NC 28400</p>
        <p>Phone (555) 201-4380</p>
        <p>Fax (555) 201-4381</p>
        <p>Email: info@holloweyfamilylaw-example.com</p>
        <p>Web: www.HolloweyFamilyLaw-example.com</p>
      </address>
    </section>
    <section class="panel panel--front">
      <div class="edge-band"><span class="edge-mark"></span></div>
      <div class="front-lockup">
        <div class="brand"><span class="brand__square"></span>Hollowey Law</div>
        <p class="tagline">Standing beside your family through<br>change and new beginnings.</p>
      </div>
    </section>
  </main>
</body>
</html>
```